Baby Organic Coconut Body Lotion

Meadow Crib Naturals is developing a line of Organic and Natural skin care products for babies and toddlers, although our skin care can also be used by adults too. These products include a body lotion, shampoo & body wash, powder, hair cream, massage body oil, bath soak, baby balm, Bar Soap, gift box and many more.
This will be an ever expanding line so the list will go on and on. We are looking forward for an eye catching designs. I attached some of our current label designs and product images. Also, we have different Baby organic body lotion and Baby organic shampoo & body wash with different fruit flavours. Coconut lotion will share the same design with the shampoo & body wash. I would like you to start with the coconut design. I have uploaded plastic bottles with different colourful caps. The bottle with the white cap is for the coconut design. the bottle with the red cap is for the strawberry design. the bottle with the orange cap is for the orange design. the bottle with the yellow cap is for the pineapple design. the bottle with the green cap is for the apple design. Bear in my mind that my baby organic skin care are made with different fruit flavours.
Target Market(s)
My target market are for mothers that wants to buy there baby and toddler skin care products.
Industry/Entity Type
Baby
Look and feel

```html
<!DOCTYPE html>
<html lang="en">
<head>
<meta charset="utf-8">
<title>Meadow Crib Naturals – Baby Organic Coconut Body Lotion</title>
<link href="https://fonts.googleapis.com/css2?family=Fredoka:wght@600&family=Dancing+Script:wght@600&family=Delius&family=Arimo:wght@400&display=swap" rel="stylesheet">
<style>
  :root {
    --page: #f4f2ef;
    --frame: #c9a289;
    --panel: #f6eee6;
    --panel-edge: #e6d3c4;
    --brand: #3d8fc6;
    --tagline: #3b6fb0;
    --rule: #c9a289;
    --pink: #d9558f;
    --brown: #4a2e22;
    --coco-light: #e9d2bd;
    --coco-dark: #6b3f28;
    --art-ring: #fbf6f1;
  }
  * { margin: 0; padding: 0; box-sizing: border-box; }
  html, body { width: 675px; height: 1200px; overflow: hidden; background: var(--page); }
  .canvas { position: relative; width: 675px; height: 1200px; }

  .label {
    position: absolute; left: 88px; top: 56px; width: 500px; height: 1088px;
    background: var(--frame);
  }
  .label__panel {
    position: absolute; left: 32px; top: 32px; right: 32px; bottom: 32px;
    background: var(--panel);
    border: 2px solid var(--panel-edge);
    text-align: center;
  }

  .brand {
    position: absolute; left: 0; right: 0; top: 50px;
    display: flex; align-items: center; justify-content: center; gap: 16px;
  }
  .brand__dot { width: 34px; height: 34px; border-radius: 50%; background: var(--brand); flex: none; }
  .brand__name {
    font-family: "Fredoka", sans-serif; font-weight: 600; font-size: 44px;
    line-height: 1.0; color: var(--brand); text-align: left;
  }
  .rule { position: absolute; left: 50px; right: 50px; top: 196px; height: 2px; background: var(--rule); }
  .tagline {
    position: absolute; left: 0; right: 0; top: 212px;
    font-family: "Arimo", sans-serif; font-size: 21px; line-height: 1.3; color: var(--tagline);
  }

  .line-kind {
    position: absolute; left: 0; right: 0; top: 372px;
    font-family: "Dancing Script", cursive; font-size: 34px; color: var(--pink);
  }
  .flavour {
    position: absolute; left: 0; right: 0; top: 428px;
    font-family: "Delius", cursive; font-size: 48px; color: var(--brown);
  }
  .product {
    position: absolute; left: 0; right: 0; top: 494px;
    font-family: "Dancing Script", cursive; font-size: 56px; color: var(--pink);
  }

  .artwork {
    position: absolute; left: 50%; top: 590px; width: 320px; height: 320px;
    margin-left: -160px; border-radius: 50%;
    background: radial-gradient(circle at 50% 50%, var(--coco-dark) 0 38%, var(--coco-light) 40% 100%);
    border: 6px solid var(--art-ring);
  }
  .volume {
    position: absolute; left: 0; right: 0; bottom: 40px;
    font-family: "Arimo", sans-serif; font-size: 22px; color: var(--brown);
  }
</style>
</head>
<body>
  <main class="canvas">
    <section class="label">
      <div class="label__panel">
        <div class="brand">
          <span class="brand__dot"></span>
          <span class="brand__name">Meadow Crib<br>Naturals</span>
        </div>
        <div class="rule"></div>
        <p class="tagline">Organic and Natural<br>Skin Care Products</p>
        <p class="line-kind">Baby Organic</p>
        <p class="flavour">Coconut</p>
        <p class="product">body lotion</p>
        <div class="artwork" role="img" aria-label="Illustration of a halved coconut"></div>
        <p class="volume">50 ml</p>
      </div>
    </section>
  </main>
</body>
</html>
```